Smart Home App Needs 4 Mockup Screens. Extra Work Guaranteed for Winner

BACKGROUND
Our company, Lumora, is launching an exciting new app early next year. And we need some examples of what our app will look like to show to some of the biggest retailers in the world. We hope that this project will lead to regular work as we have a lot of new products planned for the app.

Our app will support baby, home and pet monitors (cameras) as well as the world's first smart pet flap.

The monitors allow you to do much more than just watch live video. By monitoring and providing information on sound, movement and temperature the app provides the user with instant peace of mind wherever they are. If anything has changed the user can be alerted via notifications. If motion is detected the user will receive a clip of the whole event moments after it has happened.

The Smart Pet Flap is packed full of features too. From letting you decide when your pet can or can't go outside from your mobile, to automatically opening if a fire is detected (along with a whole host of other features) - this really is the most advanced pet flap in the world.

REQUIREMENTS
We need 4 mock-up screens creating to show the UI of our app.
1. Camera Home Page
2. Camera Notifications Page
3. Pet Flap Fire Alarm Warning Page
4. Extreme Weather Warning Page

Optional - Happy to Pay the Winner Extra for these Designs
5. Start Up/Log In Page
6. Pet Flap Notification Example
7. Pet Flap Scheduler Page (your choice)
(SEE LUMORA APP DESIGN COMPETITION - ATTACHED)

STYLE GUIDE
As you'll see from our wireframes we want our app to be very minimal and modern. The predominant colour will be white but where colour is used it should be bright (see our colour palette - which we will provide shortly).

INSPIRATION
We love the UI of Finchly (home surveillance). Also check out Vesk (smart thermostat).
(SEE LUMORA UI EXAMPLES ATTACHED)

LOGO
We love our logo. Feel free to use it in creative ways.

So far we're also using it as a kind of beacon to indicate if everything is ok.

LOGO COLOURS & APP COLOURS
As mentioned, we are thinking of using the green logo to indicate that everything is ok (and also for the pet app in general). We reserve red for when something has happened (normally bad) and needs attention, like a fire alarm going off.

The app will be predominantly black and white with the odd minimal flash of colour (probably primary colour)
We'll upload a colour scheme as soon as we have it.

CONTACT
Please message us for more details - we'll do our best to reply promptly.

FUTURE WORK
We will need extra screens made straight after the competition is over and there should be additional regular work after this.

Target Market(s)

Our app will be used by young professionals, to young parents to grandparents. The design must be contemporary but timeless and easy to use no matter how good you are with technology.

Industry/Entity Type

Pet

Font styles to use
Sans Serif

Colors
faee3f
33a6d7
ec1f27
acd036
32b7a4

Requirements
Must have
• Beautiful, minimal design. Make sure you spend time looking at the Finchly and Vesk apps before starting.

For the videos make sure you use sensible images - that you'd expect to see from a monitor (high resolution images if possible)
Nice to have
• Creative use of our logo.
Should not have
• Too much detail/clutter/colours. Ugly fonts.

```html
<!DOCTYPE html>
<html lang="en">
<head>
<meta charset="utf-8">
<title>Lumora – Camera Home</title>
<link rel="stylesheet" href="https://fonts.googleapis.com/css2?family=Open+Sans:wght@400;600;700&display=swap">
<style>
  :root {
    --bar-dark: #3a3a3a;
    --tab-dark: #3e3e3e;
    --tab-divider: #555555;
    --white: #ffffff;
    --header-tab: #f0efed;
    --text-dark: #555555;
    --text-muted: #9a9a9a;
    --teal: #32b7a4;
    --teal-light: #52c6b5;
    --grid-bg: #ebebeb;
    --logo-green: #acd036;
    --badge-red: #ec1f27;
    --icon-grey: #c9c9c9;
  }
  * { box-sizing: border-box; margin: 0; padding: 0; }
  html, body { width: 684px; height: 1200px; overflow: hidden; }
  body { font-family: "Open Sans", Arial, sans-serif; background: var(--white); }
  .screen { position: relative; width: 684px; height: 1200px; }

  .status-bar {
    height: 40px; background: var(--bar-dark); color: #e6e6e6;
    display: flex; align-items: center; justify-content: space-between;
    padding: 0 10px; font-weight: 700; font-size: 24px;
  }
  .status-left, .status-right { display: flex; align-items: center; gap: 8px; }
  .signal { display: flex; align-items: flex-end; gap: 2px; height: 16px; }
  .signal span { width: 4px; background: #e6e6e6; }

  .app-header {
    height: 81px; position: relative; background: var(--white);
    border-bottom: 1px solid #e2e2e2;
  }
  .menu-button { position: absolute; left: 50px; top: 29px; }
  .view-tab {
    position: absolute; top: 0; height: 80px; display: flex; align-items: center; justify-content: center;
    font-size: 13px; font-weight: 700; color: var(--text-dark); letter-spacing: .5px;
  }
  .view-tab--now { left: 393px; width: 124px; background: var(--header-tab); }
  .view-tab--earlier { left: 530px; width: 100px; }
  .brand {
    position: absolute; right: 8px; top: 0; height: 80px; display: flex; align-items: center; gap: 4px;
    font-size: 13px; font-weight: 700; color: var(--logo-green);
  }
  .brand-dot { width: 12px; height: 12px; border-radius: 50%; background: var(--logo-green); }

  .live-feed {
    height: 330px;
    background: linear-gradient(135deg, #e9ecf0 0%, #cfdcec 40%, #f3eee8 60%, #b9cde3 100%);
  }

  .control-band {
    height: 105px; background: var(--teal); position: relative;
  }
  .control-button {
    position: absolute; top: 12px; width: 80px; height: 80px; border-radius: 50%;
    background: var(--teal-light); display: flex; align-items: center; justify-content: center;
  }

  .camera-grid { height: 561px; background: var(--grid-bg); position: relative; }
  .camera-card { position: absolute; width: 286px; background: var(--white); }
  .camera-thumb { height: 151px; }
  .camera-label {
    height: 47px; display: flex; align-items: center; justify-content: center; gap: 22px;
    font-size: 15px; color: var(--text-muted); font-weight: 600;
  }
  .thumb-nursery { background: linear-gradient(135deg, #cfe6dc, #f4f1e8 60%, #e8d49a); }
  .thumb-patio { background: linear-gradient(135deg, #6f8a5a, #9cc06c 55%, #4a4a40); }
  .thumb-living { background: linear-gradient(135deg, #f2f2ee, #d9d3c6 55%, #c27a63); }
  .thumb-kitchen { background: linear-gradient(135deg, #f7f7f5, #e4e6e2 55%, #9fb58a); }

  .tab-bar {
    height: 83px; background: var(--tab-dark); display: flex;
  }
  .tab-item {
    flex: 1; display: flex; align-items: center; justify-content: center; position: relative;
    border-left: 1px solid var(--tab-divider);
  }
  .tab-item:first-child { border-left: none; }
  .badge {
    position: absolute; top: 18px; left: 92px; width: 18px; height: 18px; border-radius: 50%;
    background: var(--badge-red); color: var(--white); font-size: 11px; font-weight: 700;
    display: flex; align-items: center; justify-content: center;
  }
</style>
</head>
<body>
<div class="screen">
  <div class="status-bar">
    <div class="status-left">
      <div class="signal"><span style="height:5px"></span><span style="height:8px"></span><span style="height:11px"></span><span style="height:14px"></span><span style="height:16px"></span></div>
      <span>DINE</span>
    </div>
    <span>10:35 AM</span>
    <div class="status-right">
      <svg width="20" height="20" viewBox="0 0 20 20"><circle cx="10" cy="10" r="9" fill="#e6e6e6"/><path d="M10 4v6h4" stroke="#3a3a3a" stroke-width="2" fill="none"/></svg>
      <span>65%</span>
      <svg width="38" height="20" viewBox="0 0 38 20"><rect x="1" y="2" width="32" height="16" rx="2" fill="none" stroke="#e6e6e6" stroke-width="2"/><rect x="4" y="5" width="18" height="10" fill="#e6e6e6"/><rect x="34" y="7" width="3" height="6" fill="#e6e6e6"/></svg>
    </div>
  </div>

  <header class="app-header">
    <svg class="menu-button" width="34" height="22" viewBox="0 0 34 22" aria-label="Menu">
      <g fill="#555"><rect x="0" y="0" width="4" height="4"/><rect x="8" y="0" width="26" height="4"/><rect x="0" y="9" width="4" height="4"/><rect x="8" y="9" width="26" height="4"/><rect x="0" y="18" width="4" height="4"/><rect x="8" y="18" width="26" height="4"/></g>
    </svg>
    <div class="view-tab view-tab--now">NOW</div>
    <div class="view-tab view-tab--earlier">EARLIER</div>
    <div class="brand"><span class="brand-dot"></span>Lumora</div>
  </header>

  <div class="live-feed" role="img" aria-label="Live nursery camera feed of a baby sleeping on a light blue blanket"></div>

  <div class="control-band">
    <div class="control-button" style="left:58px" aria-label="Microphone">
      <svg width="34" height="44" viewBox="0 0 34 44" fill="none" stroke="#fff" stroke-width="3"><rect x="11" y="2" width="12" height="24" rx="6" fill="#fff"/><path d="M5 20a12 12 0 0 0 24 0"/><path d="M17 32v8M10 41h14"/></svg>
    </div>
    <div class="control-button" style="left:219px" aria-label="Temperature">
      <svg width="24" height="46" viewBox="0 0 24 46"><rect x="8" y="2" width="8" height="30" rx="4" fill="#fff"/><circle cx="12" cy="36" r="8" fill="#fff"/><path d="M16 10h4M16 16h4M16 22h4" stroke="#fff" stroke-width="2"/></svg>
    </div>
    <div class="control-button" style="left:380px" aria-label="Activity chart">
      <svg width="40" height="40" viewBox="0 0 40 40" fill="none" stroke="#fff" stroke-width="2.5"><path d="M3 2v35h35"/><path d="M8 30l9-11 7 6 11-16"/><circle cx="8" cy="30" r="2" fill="#fff"/><circle cx="17" cy="19" r="2" fill="#fff"/><circle cx="24" cy="25" r="2" fill="#fff"/><circle cx="35" cy="9" r="2" fill="#fff"/></svg>
    </div>
    <div class="control-button" style="left:540px" aria-label="Full screen">
      <svg width="34" height="34" viewBox="0 0 34 34" fill="none" stroke="#fff" stroke-width="3"><path d="M2 12V2h10M22 2h10v10M32 22v10H22M12 32H2V22M2 2l10 10M32 2L22 12M32 32L22 22M2 32l10-10"/></svg>
    </div>
  </div>

  <section class="camera-grid">
    <div class="camera-card" style="left:37px;top:43px">
      <div class="camera-thumb thumb-nursery" role="img" aria-label="Nursery room with shelves and window"></div>
      <div class="camera-label"><svg width="16" height="10" viewBox="0 0 16 10"><rect width="10" height="10" fill="#bbb"/><path d="M11 5l5-4v8z" fill="#bbb"/></svg>Nursery camera</div>
    </div>
    <div class="camera-card" style="left:363px;top:43px">
      <div class="camera-thumb thumb-patio" role="img" aria-label="Patio garden with a dog on the lawn"></div>
      <div class="camera-label"><svg width="16" height="10" viewBox="0 0 16 10"><rect width="10" height="10" fill="#bbb"/><path d="M11 5l5-4v8z" fill="#bbb"/></svg>Patio camera</div>
    </div>
    <div class="camera-card" style="left:37px;top:292px">
      <div class="camera-thumb thumb-living" role="img" aria-label="Bright living room with sofa and plants"></div>
      <div class="camera-label"><svg width="16" height="10" viewBox="0 0 16 10"><rect width="10" height="10" fill="#bbb"/><path d="M11 5l5-4v8z" fill="#bbb"/></svg>Living room camera</div>
    </div>
    <div class="camera-card" style="left:363px;top:292px">
      <div class="camera-thumb thumb-kitchen" role="img" aria-label="White kitchen with garden doors"></div>
      <div class="camera-label"><svg width="16" height="10" viewBox="0 0 16 10"><rect width="10" height="10" fill="#bbb"/><path d="M11 5l5-4v8z" fill="#bbb"/></svg>Kitchen camera</div>
    </div>
  </section>

  <nav class="tab-bar">
    <div class="tab-item" aria-label="Profile">
      <svg width="26" height="28" viewBox="0 0 26 28" fill="var(--icon-grey)"><circle cx="13" cy="8" r="7"/><path d="M0 28c0-8 6-12 13-12s13 4 13 12z"/></svg>
    </div>
    <div class="tab-item" aria-label="Cameras">
      <svg width="32" height="24" viewBox="0 0 32 24"><path d="M2 5h8l3-4h6l3 4h8v18H2z" fill="var(--icon-grey)"/><circle cx="16" cy="14" r="6" fill="var(--tab-dark)"/><circle cx="16" cy="14" r="3.5" fill="var(--icon-grey)"/></svg>
    </div>
    <div class="tab-item" aria-label="Settings">
      <svg width="28" height="28" viewBox="0 0 28 28"><g fill="var(--icon-grey)"><circle cx="14" cy="14" r="10"/><rect x="11" y="0" width="6" height="28" rx="1"/><rect x="0" y="11" width="28" height="6" rx="1"/><rect x="11" y="0" width="6" height="28" rx="1" transform="rotate(45 14 14)"/><rect x="11" y="0" width="6" height="28" rx="1" transform="rotate(-45 14 14)"/></g><circle cx="14" cy="14" r="4.5" fill="var(--tab-dark)"/></svg>
    </div>
    <div class="tab-item" aria-label="Notifications">
      <svg width="28" height="28" viewBox="0 0 28 28"><circle cx="14" cy="14" r="13" fill="var(--icon-grey)"/><path d="M6 8c3 0 5 2 4 5s-4 3-4 7M16 4c0 3 3 4 5 4s3 4 1 6-4 2-5 5 0 5 0 5" stroke="var(--tab-dark)" stroke-width="2.5" fill="none"/></svg>
      <span class="badge">2</span>
    </div>
  </nav>
</div>
</body>
</html>
```